Website Header for new website

We need a header/banner design for our revised website. Here is the link to our existing website lorimakwell.me and to our new website in process agewiseplus.us
Area of expertise is older adults, baby boomers and caregivers
This is an individual, professional website for a Speaker, Keynoter, Author, Brocaster

Target Market(s)

Event planners, broadcasters, publishers

Font styles to use
Serif

```html
<!DOCTYPE html>
<html lang="en">
<head>
<meta charset="utf-8">
<title>Lori Makwell – Website Header</title>
<link href="https://fonts.googleapis.com/css2?family=Lato:wght@400;700;900&family=Playball&display=swap" rel="stylesheet">
<style>
:root{
  --page:#ededed;
  --nav:#37474f;
  --nav-deep:#2f3d45;
  --warm-1:#7a5a48;
  --warm-2:#a9774f;
  --warm-3:#5d4a4a;
  --white:#ffffff;
  --tile:rgba(255,255,255,.18);
  --tile-line:rgba(255,255,255,.35);
  --script:#2e3a47;
}
*{margin:0;padding:0;box-sizing:border-box}
html,body{width:1200px;height:1200px;overflow:hidden;background:var(--page);font-family:'Lato',sans-serif;color:var(--white)}
.header{position:absolute;left:40px;top:400px;width:1120px;height:400px;overflow:hidden;
  background:linear-gradient(100deg,var(--warm-1) 0%,var(--warm-2) 35%,#8c6a5a 60%,var(--warm-3) 100%)}
.nav-bar{position:absolute;left:0;top:0;width:100%;height:73px;background:linear-gradient(90deg,var(--nav),var(--nav-deep))}
.brand{position:absolute;left:37px;top:19px;font-size:32px;font-weight:900;letter-spacing:-.3px;white-space:nowrap}
.nav-links{position:absolute;left:308px;top:29px;display:flex;gap:24px;font-size:14px;font-weight:400;white-space:nowrap}
.speaker-photo{position:absolute;left:32px;top:73px;width:258px;height:327px;
  background:linear-gradient(180deg,#c9a27f 0%,#cf5a2c 40%,#4c5256 62%,#3c4246 100%)}
.script-name{position:absolute;left:315px;top:82px;font-family:'Playball',cursive;font-size:50px;color:var(--white);white-space:nowrap;
  -webkit-text-stroke:1.5px var(--script);paint-order:stroke;text-shadow:2px 2px 0 var(--script)}
.tile{position:absolute;height:63px;border:1px solid var(--tile-line);border-radius:4px;background:var(--tile);text-align:center;line-height:1}
.tile .small{display:block;font-size:20px;margin-top:5px}
.tile .big{display:block;font-size:29px;font-weight:700;margin-top:4px}
.side-thumb{position:absolute;left:861px;width:61px;height:66px;background:linear-gradient(160deg,#6b5a4c,#2a2420)}
.side-title{position:absolute;left:930px;font-size:17px;font-weight:900;line-height:17px;white-space:nowrap}
.side-body{position:absolute;left:929px;font-size:12px;font-weight:700;line-height:14.5px;white-space:nowrap}
.footer-bar{position:absolute;left:0;top:336px;width:100%;height:64px;background:rgba(30,34,38,.9)}
.dash-box{position:absolute;border:1px dashed var(--white);border-radius:5px}
.featured{left:86px;top:12px;width:150px;height:33px;font-size:22px;font-weight:900;text-align:center;line-height:31px;white-space:nowrap}
.outlets{position:absolute;left:250px;top:24px;width:488px;display:flex;justify-content:space-between;font-size:11px;font-weight:700;white-space:nowrap}
.follow{left:750px;top:12px;width:349px;height:33px}
.follow-label{position:absolute;left:6px;top:4px;width:112px;font-size:11px;font-weight:900;line-height:12px;text-align:right;white-space:nowrap}
.social{position:absolute;top:10px;width:13px;height:13px;border-radius:50%;background:var(--white)}
.email{position:absolute;left:190px;top:8px;font-size:13px;font-weight:700;white-space:nowrap}
</style>
</head>
<body>
<header class="header">
  <div class="nav-bar">
    <div class="brand">Lori Makwell</div>
    <nav class="nav-links">
      <span>Home</span><span>Meet Lori</span><span>Speaker/Spokesperson</span><span>Podcast</span><span>Books</span><span>Work with Lori</span><span>Contact</span><span>Press</span>
    </nav>
  </div>

  <div class="speaker-photo" role="img" aria-label="Photo of the speaker in an orange jacket standing at a podium"></div>

  <div class="script-name">Lori Makwell</div>

  <div class="tile" style="left:312px;top:159px;width:152px"><span class="small">Dynatmic</span><span class="big">Keynoter</span></div>
  <div class="tile" style="left:480px;top:159px;width:152px"><span class="small">Motivating</span><span class="big">Speaker</span></div>
  <div class="tile" style="left:650px;top:159px;width:174px"><span class="small">Influential</span><span class="big">Broadcaster</span></div>
  <div class="tile" style="left:312px;top:247px;width:152px"><span class="small">Prolific</span><span class="big">Author</span></div>
  <div class="tile" style="left:480px;top:247px;width:152px"><span class="small">Enteraining</span><span class="big">Blogger</span></div>
  <div class="tile" style="left:650px;top:247px;width:174px"><span class="small">Effective</span><span class="big">Trainer</span></div>

  <div class="side-thumb" style="top:119px" role="img" aria-label="Portrait of the latest podcast guest"></div>
  <div class="side-title" style="top:115px">OUR LATEST<br>PODCAST</div>
  <div class="side-body" style="top:160px">Podcast Guest:<br>Nora Delwyn, ELDA<br>AgeWise Plus Radio,<br>July 26–Guest:<br>Nora Delwyn, ...Click Here</div>

  <div class="side-thumb" style="top:249px" role="img" aria-label="Photo of the speaker at a speaking engagement"></div>
  <div class="side-title" style="top:249px">SPEAKER/<br>SPOKESPERSON</div>
  <div class="side-body" style="top:290px;left:931px;font-size:13px">Topics &amp; Testimonials</div>

  <div class="footer-bar">
    <div class="dash-box featured">FEATURD ON</div>
    <div class="outlets">
      <span>FinWire</span><span>Daylight Talk</span><span>Ledger Radio</span><span>WKRT 77AM</span><span>WLNV 570AM</span><span>Relay One</span>
    </div>
    <div class="dash-box follow">
      <div class="follow-label">FOLLOW US<br>ON SOCIAL MEDIA</div>
      <span class="social" style="left:125px"></span>
      <span class="social" style="left:146px"></span>
      <span class="social" style="left:167px"></span>
      <span class="email">lori@lorimakwell.me</span>
    </div>
  </div>
</header>
</body>
</html>
```